Stationary - Business Card/Letterhead and envelope design

Details for my new Stationery Design Project will be added soon. , I have two logos I am trying to decide on. I will upload the eps logos shortly. I have attached a file of what i have so far. I need urgently Business cards, but also will need a letterhead template and envelopes.

PLEASE NOTE THE DEADLINE SAYS 2 DAYS but I need business card design in LESS THAN A DAY.

thanks, Details for my new Stationery Design Project will be added soon. , I have two logos I am trying to decide on. I will upload the eps logos shortly. I have attached a file of what i have so far. I need urgently Business cards, but also will need a letterhead template and envelopes.

thanks
Updates

I have uploaded one of the logos you can work with. hopefully the other one comes soon.

details for the business card.

Marla Thorne

Managing Director

P&K Ventures Ltd

Bda: 1-441-555-0193

Email: marla@pkvnbda.com

web: www.pkvnbda.com

Industry/Entity Type

Business

```html
<!DOCTYPE html>
<html lang="en">
<head>
<meta charset="utf-8">
<title>P&amp;K Ventures — Business Card</title>
<link href="https://fonts.googleapis.com/css2?family=Arimo:wght@400&family=Libre+Baskerville:wght@700&display=swap" rel="stylesheet">
<style>
  :root {
    --backdrop: #e9e4de;
    --card-white: #ffffff;
    --brand-teal: #5cb2cb;
    --brand-brown: #77685b;
    --ink: #2a2a2a;
    --card-dark: #1f3c43;
    --card-dark-raised: #27464e;
  }
  * { box-sizing: border-box; margin: 0; padding: 0; }
  html, body {
    width: 1200px; height: 1023px; overflow: hidden;
    background: var(--backdrop);
    font-family: "Arimo", Arial, sans-serif;
  }
  .canvas { position: relative; width: 1200px; height: 1023px; }

  .card {
    position: absolute; width: 560px; height: 320px;
    box-shadow: 0 6px 18px rgba(0,0,0,0.18);
  }
  .card--front { left: 60px; top: 120px; background: var(--card-white); }
  .card--back  { left: 580px; top: 580px; background: var(--card-dark); }

  .edge-tab {
    position: absolute; width: 12px; height: 34px; background: var(--brand-brown);
  }
  .edge-tab--left  { left: 0; top: 24px; }
  .edge-tab--right { right: 0; bottom: 24px; }

  .wordmark {
    position: absolute; left: 48px; top: 104px;
    font-family: "Libre Baskerville", Georgia, serif; font-weight: 700;
    font-size: 44px; line-height: 1.1; color: var(--brand-teal);
    letter-spacing: -1px;
  }

  .person { position: absolute; right: 44px; top: 34px; text-align: right; }
  .person__name {
    font-family: "Libre Baskerville", Georgia, serif; font-weight: 700;
    font-size: 20px; color: var(--brand-teal);
  }
  .person__title { font-size: 13px; color: var(--ink); margin-top: 3px; }

  .contact { position: absolute; right: 44px; top: 130px; list-style: none; }
  .contact li {
    display: flex; justify-content: flex-end; align-items: center; gap: 10px;
    font-size: 14px; color: var(--ink); line-height: 26px;
  }
  .contact svg { width: 10px; height: 10px; fill: var(--brand-teal); }

  .address {
    position: absolute; left: 48px; bottom: 30px;
    font-size: 14px; line-height: 18px; color: var(--ink);
  }
  .address__company { color: #000; }

  .back-wordmark {
    position: absolute; inset: 0; display: flex; align-items: center; justify-content: center;
    font-family: "Libre Baskerville", Georgia, serif; font-weight: 700;
    font-size: 64px; color: var(--card-dark-raised); letter-spacing: -1px;
  }
</style>
</head>
<body>
<main class="canvas">
  <section class="card card--front" aria-label="Business card front">
    <span class="edge-tab edge-tab--left"></span>
    <span class="edge-tab edge-tab--right"></span>

    <div class="wordmark">P&amp;K Ventures</div>

    <div class="person">
      <p class="person__name">Marla Thorne</p>
      <p class="person__title">Managing Director</p>
    </div>

    <ul class="contact">
      <li>1-441-555-0193
        <svg viewBox="0 0 10 10" aria-hidden="true"><path d="M2 0h2l1 3-1.5 1a6 6 0 0 0 2.5 2.5L7 5l3 1v2a2 2 0 0 1-2 2A8 8 0 0 1 0 2a2 2 0 0 1 2-2z"/></svg>
      </li>
      <li>marla@pkvnbda.com
        <svg viewBox="0 0 10 10" aria-hidden="true"><rect x="0" y="2" width="10" height="7"/></svg>
      </li>
      <li>www.pkvnbda.com
        <svg viewBox="0 0 10 10" aria-hidden="true"><circle cx="5" cy="5" r="5"/></svg>
      </li>
    </ul>

    <address class="address" style="font-style:normal">
      <span class="address__company">P&amp;K Ventures Ltd</span><br>
      Your Local Address<br>
      Goes in Here
    </address>
  </section>

  <section class="card card--back" aria-label="Business card back">
    <div class="back-wordmark">P&amp;K Ventures</div>
  </section>
</main>
</body>
</html>
```